PETAL Project Roll Up Banner 85x200 cm (1:10, 1200 dpi)

PETAL is a EU-funded project to promote female entrepreneurship networks. The project is developed by 9 partners from 7 different countries.
The banner is to be used throughout the project in exhibitions, conferences, roundtables, etc.
It has to include the following graphic elements, which cannot be modified beyond scaling:
- PETAL logo
- EU logo (cannot be modified in any way, and cannot have any kind of background, but pure white).
- 9 partners logos
- Friendlane link (with logo)
- Workmesh link (with logo)
- Project's website (www.petal-circlehub.eu)
The text to be included:
Pioneering Enterprising Talent And Leadership
PETAL: Contributes to the strengthening of the links between women entrepreneurs and the mainstream of new technologies, educational, and training practices offered all over Europe.
GOOD PRACTICES: Compilation of EU projects promoting female entrepreneurship and ICT systems for learning, supporting, and training women entrepreneurs.
NETWORK: Strengthening of linkages between EU women entrepreneurs, project managers, learning communities, multipliers, and society to encourage a knowledge-sharing environment through the creation of the PETAL network.
ONE-STOP SHOP: Development of a multi-lingual EU online platform, where valuable an innovative EU learning opportunities can be found and accessed at one single place, as well as fostering new business opportunities by a Virtual Market.
The banner has to be attractive the modern female entrepreneur. It has to be easy to read, and present a fresh and exciting identity.
The banner has to include 5 additional centimetres on the top, and 10 on the bottom.
The last partner logo has been uploaded now.
Female entrepreneurs
Higher Educational Institutions
Government Female Representatives
Environment

```html
<!DOCTYPE html>
<html lang="en">
<head>
<meta charset="utf-8">
<title>PETAL Roll Up Banner</title>
<link rel="stylesheet" href="https://fonts.googleapis.com/css2?family=Questrial&family=Mulish:wght@700;800&display=swap">
<style>
  :root {
    --cyan: #16aee8;
    --ink: #231f20;
    --white: #ffffff;
    --pink: #e5177e;
    --navy: #2b4a8f;
    --eu-blue: #1f4fa3;
    --text-dark: #2a2a2a;
    --page: #ffffff;
  }
  * { box-sizing: border-box; margin: 0; padding: 0; }
  html, body {
    width: 1200px; height: 1000px; overflow: hidden;
    background: var(--page);
  }
  .canvas { position: relative; width: 1200px; height: 1000px; }
  .banner {
    position: absolute; left: 400px; top: 29px;
    width: 400px; height: 942px;
    background: var(--white);
    border: 1px solid #d0d0d0;
    overflow: hidden;
    font-family: "Mulish", sans-serif;
  }
  .band-top { position: absolute; left: 0; top: 0; width: 100%; height: 24px; background: var(--cyan); }
  .band-bottom { position: absolute; left: 0; top: 881px; width: 100%; height: 61px; background: var(--cyan); }

  .header { position: absolute; left: 0; top: 24px; width: 100%; height: 128px; }
  .brand {
    position: absolute; left: 26px; top: 46px;
    display: flex; align-items: center; gap: 10px;
    font-family: "Questrial", sans-serif; font-size: 40px; letter-spacing: 2px;
    color: var(--navy);
  }
  .brand-dot { width: 14px; height: 14px; border-radius: 50%; background: var(--cyan); }
  .programme {
    position: absolute; left: 202px; top: 44px;
    display: flex; align-items: center; gap: 9px;
  }
  .programme-mark { width: 66px; height: 48px; background: var(--eu-blue); }
  .programme-name {
    font-family: "Questrial", sans-serif; font-size: 16px; line-height: 1.08;
    color: var(--eu-blue);
  }

  .panel { position: absolute; left: 0; top: 152px; width: 100%; height: 619px; background: var(--ink); }
  .panel svg.dome { position: absolute; left: 0; top: 388px; }

  .tagline {
    position: absolute; left: 14px; top: 24px; width: 372px;
    font-family: "Questrial", sans-serif; font-size: 20px; line-height: 27px;
    color: var(--pink); text-align: center;
  }
  .tagline .mark { font-size: 30px; line-height: 0; vertical-align: -6px; }

  .pillars { position: absolute; left: 16px; top: 118px; width: 370px; }
  .pillar {
    font-size: 9.6px; line-height: 13.6px; color: var(--white);
    margin-bottom: 12px;
  }
  .pillar-label { color: var(--cyan); font-weight: 800; }

  .partners { position: absolute; left: 0; top: 420px; width: 100%; }
  .partners-title {
    font-family: "Questrial", sans-serif; font-size: 21px; font-weight: 700;
    color: var(--cyan); text-align: center;
  }
  .partner-grid {
    display: grid; grid-template-columns: repeat(3, 1fr);
    row-gap: 20px; padding: 22px 18px 0; justify-items: center; align-items: center;
  }
  .partner-badge { height: 28px; border-radius: 3px; }

  .web-band { position: absolute; left: 0; top: 771px; width: 100%; height: 35px; background: var(--ink); }
  .website {
    text-align: center; line-height: 35px;
    font-size: 20px; font-weight: 800; color: var(--pink);
  }

  .social { position: absolute; left: 16px; top: 814px; }
  .social-link {
    display: flex; align-items: center; gap: 14px;
    font-size: 14px; font-weight: 800; color: var(--text-dark);
    height: 30px; margin-bottom: 3px;
  }
  .social-dot { width: 26px; height: 26px; border-radius: 50%; background: var(--navy); }
</style>
</head>
<body>
<div class="canvas">
  <div class="banner">
    <div class="band-top"></div>

    <header class="header">
      <div class="brand"><span class="brand-dot"></span>PETAL</div>
      <div class="programme">
        <div class="programme-mark"></div>
        <div class="programme-name">Continuous<br>Study<br>Scheme</div>
      </div>
    </header>

    <section class="panel">
      <p class="tagline"><span class="mark">“</span> Pioneering Enterprising Talent<br>And Leadership.<span class="mark">”</span></p>

      <div class="pillars">
        <p class="pillar"><span class="pillar-label">PETAL:</span> Contributes to the strengthening of the links between women entrepreneurs and the mainstream of new technologies, educational, and training practices offered all over Europe.</p>
        <p class="pillar"><span class="pillar-label">GOOD PRACTICES:</span> Compilation of EU projects promoting female entrepreneurship and ICT systems for learning, supporting, and training women entrepreneurs.</p>
        <p class="pillar"><span class="pillar-label">NETWORK:</span> Strengthening of linkages between EU women entrepreneurs, project managers, learning communities, multipliers, and society to encourage a knowledge-sharing environment through the creation of the PETAL network.</p>
        <p class="pillar"><span class="pillar-label">ONE-STOP SHOP:</span> Development of a multi-lingual EU online platform, where valuable an innovative EU learning opportunities can be found and accessed at one single place, as well as fostering new business opportunities by a Virtual Market.</p>
      </div>

      <svg class="dome" width="400" height="231" viewBox="0 0 400 231" aria-hidden="true">
        <path d="M0 80 C60 10 340 10 400 80 L400 231 L0 231 Z" fill="#ffffff"/>
      </svg>

      <div class="partners">
        <h2 class="partners-title">Partners</h2>
        <div class="partner-grid">
          <div class="partner-badge" style="width:90px;background:#8fc640"></div>
          <div class="partner-badge" style="width:96px;background:#1d3f8f"></div>
          <div class="partner-badge" style="width:110px;background:#3b3b3b"></div>
          <div class="partner-badge" style="width:92px;background:#2a77b9"></div>
          <div class="partner-badge" style="width:78px;background:#f08c1e"></div>
          <div class="partner-badge" style="width:108px;background:#d2232a"></div>
          <div class="partner-badge" style="width:58px;height:36px;background:#5aa33c"></div>
          <div class="partner-badge" style="width:74px;background:#7ab648"></div>
          <div class="partner-badge" style="width:112px;background:#c9d84a"></div>
        </div>
      </div>
    </section>

    <div class="web-band"><p class="website">www.petal-circlehub.eu</p></div>

    <div class="social">
      <div class="social-link"><span class="social-dot"></span>www.friendlane.com/petal.circle</div>
      <div class="social-link"><span class="social-dot"></span>www.workmesh.com/groups/PETALCIRCLE-4417302</div>
    </div>

    <div class="band-bottom"></div>
  </div>
</div>
</body>
</html>
```